Flat Belly Design Graphics for Social

I want to create 9 social media graphics (new Instagram size 4:5 (1080 x 1350 pixels) focusing on our Flat Belly Graphics, using the pics attached. Use the attached pics, NO RANDOM STOCK PHOTOGRAPHY. For the color scheme of the graphics, the color palette is attached. YOU MUST POST ALL 9 GRAPHICS IN ONE ENTRY.
Using the 3 titles below, create one set of graphics. 1) with all text, then for the others, use the pictures as detailed below in IMPORTANT:
1. 21-Night Lean Middle Reboot Beyond 50
2. The 20-Second Trim-Core Menu Guide
3. Starlet Tricks to a Slender Midline Beyond 50 - Zero Scalpel Needed
IMPORTANT:
Only use RK Pic 1 and RK Pic 2 with the title, 21-Night Lean Middle Reboot Beyond 50
Only use meal plan1 and meal plan2 pics with the title, 20-Second Trim-Core Menu Guide
Only use starlet tricks 1 and starlet tricks 2 pics with the title, Starlet Tricks to a Slender Midline Beyond 50 - Zero Scalpel Needed
women over 40

```html
<!DOCTYPE html>
<html lang="en">
<head>
<meta charset="utf-8">
<title>Lean Middle Social Set</title>
<link rel="stylesheet" href="https://fonts.googleapis.com/css2?family=Anton&family=Archivo+Black&family=Damion&family=Kaushan+Script&family=Oswald:wght@600;700&display=swap">
<style>
:root{
  --board:#25092f;
  --pink:#f29ac0;
  --pink-soft:#fbd6e5;
  --pink-pale:#fdeaf2;
  --hot:#e0359a;
  --teal:#0d8a86;
  --teal-deep:#0b6b68;
  --white:#ffffff;
  --wood:#5a3520;
}
*{box-sizing:border-box;margin:0;padding:0}
html,body{width:984px;height:1200px;overflow:hidden;background:var(--board)}
.board{position:relative;width:984px;height:1200px;background:var(--board)}
.panel{position:absolute;width:293px;height:365px;overflow:hidden}
.c1{left:37px}.c2{left:347px}.c3{left:658px}
.r1{top:31px}.r2{top:414px}.r3{top:799px}
.line{position:absolute;left:0;width:100%;text-align:center;line-height:1;white-space:nowrap}
.photo{position:absolute}
.condensed{font-family:"Anton",Impact,sans-serif}
.heavy{font-family:"Archivo Black","Arial Black",sans-serif}
.tall{font-family:"Oswald","Arial Narrow",sans-serif;font-weight:700}
.brush{font-family:"Kaushan Script",cursive}
.script{font-family:"Damion",cursive}
.stroke-w{-webkit-text-stroke:5px var(--white);paint-order:stroke fill}
.stroke-p{-webkit-text-stroke:5px var(--hot);paint-order:stroke fill}
.chip{display:inline-block;background:var(--white);color:var(--teal);border:3px solid var(--pink);border-radius:6px;padding:1px 6px 0}
.ghost{position:absolute;left:0;width:100%;text-align:center;font-family:"Archivo Black",sans-serif;font-size:38px;color:transparent;-webkit-text-stroke:1px rgba(255,255,255,.55);line-height:1.05;white-space:nowrap}
svg.shape{position:absolute;left:0;top:0}
</style>
</head>
<body>
<main class="board">

  <!-- Row 1 -->
  <section class="panel c1 r1 starlet-split" style="background:linear-gradient(#f6a9c9,#f08fbb)">
    <svg class="shape" width="293" height="365"><polygon points="0,140 293,100 293,365 160,365 0,260" fill="var(--teal)"/></svg>
    <div class="photo" role="img" aria-label="Photo of two women sharing a whispered secret" style="left:50px;top:112px;width:200px;height:200px;border-radius:8px;background:linear-gradient(135deg,#e8c0a8,#d9a7b6 55%,#8ab7c8)"></div>
    <div class="line condensed" style="top:8px;font-size:31px;color:var(--white)">STARLET TRICKS</div>
    <div class="line heavy" style="top:45px;font-size:16px;color:var(--white)">TO A SLENDER</div>
    <div class="line brush" style="top:64px;font-size:26px;color:var(--white)">Midline <span style="color:var(--teal)">Beyond 50</span></div>
    <div class="line heavy stroke-w" style="top:285px;font-size:26px;color:var(--teal)">ZERO SCALPEL</div>
    <div class="line heavy stroke-w" style="top:315px;font-size:26px;color:var(--teal)">NEEDED</div>
  </section>

  <section class="panel c2 r1 menu-over-food">
    <div class="photo" role="img" aria-label="Photo of a blank menu sheet on a wooden table with fruit, chicken and vegetables" style="inset:0;background:radial-gradient(circle at 50% 75%,#f4f1ee 0 28%,transparent 29%),linear-gradient(135deg,#c9433e,#7a4a2a 45%,var(--wood) 70%,#8a6a3a)"></div>
    <div class="line heavy stroke-w" style="top:14px;font-size:22px;color:var(--hot)">The 20-Second</div>
    <div class="line heavy stroke-w" style="top:46px;font-size:38px;color:var(--teal)">TRIM-CORE</div>
    <div class="line heavy stroke-w" style="top:95px;font-size:28px;color:var(--hot)">Menu Guide</div>
  </section>

  <section class="panel c3 r1 reboot-portrait" style="background:linear-gradient(#f7b3cf,#f3a0c4);border:6px solid #f6c1d7">
    <div class="photo" role="img" aria-label="Photo of a smiling woman in a cropped white sweater pointing at her waist" style="left:40px;top:80px;width:201px;height:279px;background:linear-gradient(#3a2a2a 0 25%,#f6f1f3 25% 72%,#7a5040 72%)"></div>
    <div class="line" style="top:10px;font-size:34px"><span class="chip heavy">21</span> <span class="script" style="color:var(--teal);font-size:36px">-Night</span></div>
    <div class="line heavy stroke-w" style="top:62px;font-size:30px;color:var(--teal)">LEAN MIDDLE</div>
    <div class="line script stroke-w" style="top:292px;font-size:40px;color:var(--hot)">Reboot Beyond 50</div>
  </section>

  <!-- Row 2 -->
  <section class="panel c1 r2 menu-band" style="background:var(--wood)">
    <div class="photo" role="img" aria-label="Photo of a blank menu sheet surrounded by chicken, berries and asparagus" style="inset:0;background:radial-gradient(circle at 70% 78%,#f4f1ee 0 26%,transparent 27%),linear-gradient(135deg,#e7b39e,#7a4a2a 40%,#c4413d 60%,var(--wood))"></div>
    <svg class="shape" width="293" height="365"><polygon points="0,0 293,0 293,135 130,168 0,145" fill="var(--hot)"/></svg>
    <div class="line heavy" style="top:14px;font-size:24px;color:var(--white)">The <span class="chip" style="font-size:20px">20</span> -Second</div>
    <div class="line heavy stroke-w" style="top:52px;font-size:36px;color:var(--teal)">TRIM-CORE</div>
    <div class="line tall" style="top:102px;font-size:34px;color:var(--white)">Menu Guide</div>
  </section>

  <section class="panel c2 r2 reboot-framed" style="background:var(--white);padding:10px">
    <div style="position:absolute;inset:10px;background:linear-gradient(#f6a6c8,#fbd1e2)"></div>
    <div class="ghost" style="top:14px">LEAN MIDDLE<br>LEAN MIDDLE<br>LEAN MIDDLE<br>LEAN MIDDLE</div>
    <div class="photo" role="img" aria-label="Photo of a smiling woman in a cropped white sweater pointing at her waist" style="left:42px;top:20px;width:210px;height:250px;background:linear-gradient(#3a2a2a 0 30%,#f6f1f3 30% 85%,#7a5040 85%)"></div>
    <div class="line" style="top:214px;font-size:32px"><span class="chip heavy">21</span> <span class="script" style="color:var(--teal);font-size:34px">-Night</span></div>
    <div class="line heavy stroke-w" style="top:262px;font-size:30px;color:var(--teal)">LEAN MIDDLE</div>
    <div class="line script stroke-w" style="top:305px;font-size:32px;color:var(--hot)">Reboot Beyond 50</div>
  </section>

  <section class="panel c3 r2 starlet-light" style="background:linear-gradient(#fbe3ee,#f7c9dc)">
    <div class="photo" role="img" aria-label="Photo of two women sharing a whispered secret" style="left:50px;top:95px;width:200px;height:210px;border-radius:8px;background:linear-gradient(135deg,#e8c0a8,#d9a7b6 55%,#8ab7c8)"></div>
    <div class="line" style="top:14px;font-size:24px"><span class="heavy" style="color:var(--hot)">STARLET</span> <span class="brush" style="color:var(--teal);font-size:28px">Tricks</span></div>
    <div class="line heavy" style="top:48px;font-size:16px;color:var(--hot)">TO A SLENDER</div>
    <div class="line brush" style="top:66px;font-size:26px;color:var(--teal)">Midline Beyond 50</div>
    <div class="line heavy stroke-p" style="top:283px;font-size:26px;color:var(--teal)">ZERO SCALPEL</div>
    <div class="line heavy stroke-p" style="top:313px;font-size:26px;color:var(--teal)">NEEDED</div>
  </section>

  <!-- Row 3 -->
  <section class="panel c1 r3 reboot-white" style="background:var(--white);border:6px solid var(--pink-soft)">
    <div class="ghost" style="top:108px;-webkit-text-stroke:1px #f1d4df">LEAN MIDDLE<br>LEAN MIDDLE<br>LEAN MIDDLE<br>LEAN MIDDLE</div>
    <div class="photo" role="img" aria-label="Photo of a smiling woman in a cropped white sweater pointing at her waist" style="left:40px;top:75px;width:201px;height:280px;background:linear-gradient(#3a2a2a 0 25%,#f6f1f3 25% 75%,#7a5040 75%)"></div>
    <div class="line" style="top:10px"><span class="chip heavy" style="font-size:28px">21-NIGHT</span></div>
    <div class="line tall" style="top:50px;font-size:44px;color:var(--hot)">LEAN MIDDLE</div>
    <div class="line script stroke-w" style="top:290px;font-size:40px;color:var(--hot)">Reboot Beyond 50</div>
  </section>

  <section class="panel c2 r3 starlet-curve" style="background:linear-gradient(#f6a9c9,#f08fbb)">
    <svg class="shape" width="293" height="365"><path d="M0,215 Q146,150 293,215 V365 H0Z" fill="var(--teal)"/></svg>
    <div class="photo" role="img" aria-label="Photo of two women sharing a whispered secret" style="left:50px;top:110px;width:200px;height:200px;border-radius:8px;background:linear-gradient(135deg,#e8c0a8,#d9a7b6 55%,#8ab7c8)"></div>
    <div class="line condensed" style="top:8px;font-size:31px;color:var(--white)">STARLET TRICKS</div>
    <div class="line heavy" style="top:45px;font-size:16px;color:var(--white)">TO A SLENDER</div>
    <div class="line brush" style="top:64px;font-size:26px;color:var(--white)">Midline <span style="color:var(--teal)">Beyond 50</span></div>
    <div class="line heavy stroke-w" style="top:285px;font-size:26px;color:var(--teal)">ZERO SCALPEL</div>
    <div class="line heavy stroke-w" style="top:315px;font-size:26px;color:var(--teal)">NEEDED</div>
  </section>

  <section class="panel c3 r3 menu-bottom" style="background:linear-gradient(#fbe3ee,#f7c4d9);border:6px solid var(--teal-deep)">
    <div class="photo" role="img" aria-label="Photo of a blank menu sheet on a wooden table with chickpeas and asparagus" style="left:0;top:0;width:100%;height:200px;clip-path:polygon(0 0,100% 0,100% 68%,0 100%);background:radial-gradient(circle at 48% 45%,#f4f1ee 0 30%,transparent 31%),linear-gradient(135deg,#e7b39e,#6a8a3a 35%,var(--wood) 60%,#c8a050)"></div>
    <svg class="shape" width="293" height="365"><polygon points="0,196 281,130 281,137 0,204" fill="var(--teal)"/></svg>
    <div class="line heavy" style="top:222px;font-size:24px;color:var(--teal)">The <span class="chip" style="font-size:20px">20</span> -Second</div>
    <div class="line heavy stroke-w" style="top:258px;font-size:36px;color:var(--hot)">TRIM-CORE</div>
    <div class="line tall" style="top:302px;font-size:34px;color:var(--teal)">Menu Guide</div>
  </section>

</main>
</body>
</html>
```